Business Card Design Project

Financial planning, Insurance and Real estate - Financial Services company

Contact Information for Business Card

Looking for something simple in design -
Tolverin Equity LLC
Tolverin Wealth Managment

```html
<!DOCTYPE html>
<html lang="en">
<head>
<meta charset="utf-8">
<title>Tolverin Wealth Managment – Business Card</title>
<link rel="stylesheet" href="https://fonts.googleapis.com/css2?family=Roboto+Condensed:wght@700&family=Open+Sans:wght@400;600&display=swap">
<style>
  :root {
    --brand-blue: #1b7fc2;
    --card-white: #ffffff;
    --backdrop: #e8ecef;
    --shadow: rgba(20, 40, 60, 0.18);
  }
  * { margin: 0; padding: 0; box-sizing: border-box; }
  html, body {
    width: 1200px;
    height: 720px;
    overflow: hidden;
    background: var(--backdrop);
  }
  .stage {
    width: 1200px;
    height: 720px;
    display: flex;
    justify-content: center;
    align-items: center;
    gap: 60px;
  }
  .card {
    width: 340px;
    height: 560px;
    border-radius: 26px;
    overflow: hidden;
    box-shadow: 0 10px 28px var(--shadow);
    background: var(--brand-blue);
  }
  .card svg { display: block; }
  .brand-name {
    font-family: "Roboto Condensed", "Arial Narrow", sans-serif;
    font-weight: 700;
    font-size: 19px;
    fill: var(--brand-blue);
  }
  .holder-name {
    font-family: "Open Sans", Arial, sans-serif;
    font-weight: 600;
    font-size: 14px;
    fill: var(--card-white);
    letter-spacing: 0.5px;
  }
  .holder-title {
    font-family: "Open Sans", Arial, sans-serif;
    font-size: 11.5px;
    fill: var(--card-white);
  }
  .contact-line {
    font-family: "Open Sans", Arial, sans-serif;
    font-size: 11.5px;
    fill: var(--card-white);
  }
  .contact-icon { fill: var(--card-white); }
  .contact-glyph { fill: var(--brand-blue); }
</style>
</head>
<body>
<main class="stage">

  <section class="card card-front" aria-label="Card front">
    <svg width="340" height="560" viewBox="0 0 340 560">
      <rect class="card-base" width="340" height="560" fill="var(--brand-blue)"/>
      <g class="swoosh-stripes" fill="var(--card-white)">
        <path d="M150 0 C 190 60, 230 110, 300 150 L 280 150 C 215 115, 175 65, 130 0 Z"/>
        <path d="M180 0 C 215 55, 255 100, 340 130 L 340 140 C 250 112, 205 62, 165 0 Z"/>
        <path d="M215 0 C 245 45, 285 80, 340 100 L 340 108 C 280 88, 238 52, 204 0 Z"/>
      </g>
      <path class="white-dome" fill="var(--card-white)"
            d="M0 150 C 60 120, 280 120, 340 170 L 340 560 L 0 560 Z"/>
      <g class="brand-mark" transform="translate(170 330)">
        <circle r="46" fill="none" stroke="var(--brand-blue)" stroke-width="6"/>
      </g>
      <text class="brand-name" transform="translate(95 300) rotate(90)">Tolverin Wealth Managment</text>
    </svg>
  </section>

  <section class="card card-back" aria-label="Card back">
    <svg width="340" height="560" viewBox="0 0 340 560">
      <rect class="card-base" width="340" height="560" fill="var(--brand-blue)"/>
      <path class="white-panel" fill="var(--card-white)"
            d="M0 0 L 250 0 L 250 150 C 250 260, 190 330, 90 330 L 0 330 Z"/>
      <g class="swoosh-stripes" fill="var(--card-white)">
        <path d="M165 332 C 240 342, 295 365, 340 392 L 340 404 C 290 376, 235 354, 155 343 Z"/>
        <path d="M212 318 C 268 324, 312 338, 340 352 L 340 361 C 308 346, 264 334, 205 328 Z"/>
      </g>

      <text class="brand-name" transform="translate(40 70) rotate(90)">Tolverin Wealth Managment</text>
      <g class="brand-mark" transform="translate(150 140)">
        <circle r="46" fill="none" stroke="var(--brand-blue)" stroke-width="6"/>
      </g>

      <g class="contact-block">
        <text class="holder-name" transform="translate(298 420) rotate(90)">Dana Merrow</text>
        <text class="holder-title" transform="translate(276 420) rotate(90)">Senior Advisor</text>

        <circle class="contact-icon" cx="245" cy="422" r="7"/>
        <path class="contact-glyph" d="M242 419 l6 0 l-3 6 z"/>
        <text class="contact-line" transform="translate(240 436) rotate(90)">42 Ridgeway Avenue</text>

        <circle class="contact-icon" cx="205" cy="422" r="7"/>
        <rect class="contact-glyph" x="202" y="418" width="6" height="8" rx="1.5"/>
        <text class="contact-line" transform="translate(200 436) rotate(90)">111 111 1111</text>

        <circle class="contact-icon" cx="165" cy="422" r="7"/>
        <rect class="contact-glyph" x="161" y="419" width="8" height="6" rx="1"/>
        <text class="contact-line" transform="translate(160 436) rotate(90)">info@tolverin.com</text>

        <circle class="contact-icon" cx="125" cy="422" r="7"/>
        <circle class="contact-glyph" cx="125" cy="422" r="3.5"/>
        <text class="contact-line" transform="translate(120 436) rotate(90)">www.tolverin.com</text>
      </g>
    </svg>
  </section>

</main>
</body>
</html>
```